We are full service plumbing contractors that are capable of performing all of your plumbing need...

A clean, crisp website that conveys we can handle any plumbing from drain cleaning, repairs, to new construction. But emphasis on Leak detection, under-slab and underground water service leaks, repairs, and reroutes. Leak detection by acoustical, Thermal, or tracer gas , methods.Also emphasize advanced drain cleaning technologies and equipment. Don't just poke ahole in the drain blockage, Clean the pipe, with our High pressure hydrojetters, or Chain knocker drain cables that expand to the width of the pipe being cleaned.

Number of Pages Required

5+ page

Font styles to use
Sans Serif

Requirements
Should not have
• Canned photos

```html
<!DOCTYPE html>
<html lang="en">
<head>
<meta charset="utf-8">
<title>Harbor Pipe – Home Page Design</title>
<link rel="stylesheet" href="https://fonts.googleapis.com/css2?family=Gelasio&family=Jost:wght@400;500;600;700&display=swap">
<style>
  :root{
    --blue:#0f75bd;
    --sky:#21abe1;
    --ink:#363636;
    --grey:#8a8a8a;
    --board:#eeeeee;
    --white:#ffffff;
    --serif:"Gelasio", Georgia, serif;
    --sans:"Jost", "Futura", sans-serif;
  }
  *{box-sizing:border-box;margin:0;padding:0}
  html,body{width:1200px;height:3409px;overflow:hidden}
  body{position:relative;background:linear-gradient(var(--white) 0 443px,var(--board) 443px);font-family:var(--sans);color:var(--ink)}
  .board-title{position:absolute;left:0;width:1200px;text-align:center;font-weight:700;font-size:32px;letter-spacing:1px;color:#111}
  .board-title.responsive{top:10px}
  .board-title.home{top:1028px}

  .guide-label{position:absolute;top:660px;font-weight:700;font-size:40px;color:#111}
  .guide-label.font{left:59px}
  .guide-label.color{left:936px}
  .font-list{position:absolute;left:68px;top:722px;border-left:2px solid #c9d6c9;padding-left:20px;height:170px}
  .font-list li{list-style:none;font-size:30px;line-height:55px;color:#555}
  .font-list .georgia{font-family:var(--serif);letter-spacing:1px}
  .font-list .heavy{font-weight:700;font-size:28px;color:#333}
  .font-list .book{font-size:27px;letter-spacing:1px;color:#666}
  .swatch{position:absolute;left:936px;width:132px;height:41px;color:#fff;font-size:11px;display:flex;align-items:center;justify-content:center}

  .page{position:absolute;left:64px;top:1097px;width:1080px;height:2277px;background:var(--white);overflow:hidden;box-shadow:0 0 14px rgba(0,0,0,.08)}
  .page > *{position:absolute}
  .hero{left:0;top:0;width:1080px;height:505px;background:linear-gradient(135deg,#f4f5f6,#e6e8ea 55%,#f2f3f4)}
  .nav{left:145px;top:15px;display:flex;gap:0;font-size:10px;font-weight:600;text-transform:uppercase;color:#222}
  .nav a{position:absolute;color:inherit;text-decoration:none;white-space:nowrap}
  .nav .active::after{content:"";position:absolute;left:-2px;right:-2px;top:22px;height:3px;background:var(--sky)}
  .brand{display:flex;align-items:center;gap:12px;font-family:var(--sans);font-weight:700;color:var(--blue)}
  .brand .dot{width:16px;height:16px;border-radius:50%;background:var(--sky)}
  .hero-brand{left:0;width:1080px;top:192px;justify-content:center;font-size:56px}

  .photo{background:linear-gradient(160deg,#9aa79a,#c8ccc6 45%,#6f7470);box-shadow:0 6px 18px rgba(0,0,0,.25)}
  .van{left:118px;top:402px;width:318px;height:284px;background:linear-gradient(170deg,#5f7d4f,#a9b3a5 40%,#e8ecee 60%,#7c7f7e)}
  h2{font-family:var(--serif);font-weight:400;color:#222;font-size:36px;line-height:1.1}
  .lead{font-weight:600;color:var(--sky);font-size:13.5px;line-height:23px}
  .body{color:var(--grey);font-size:11px;line-height:15px}
  .more{font-size:11px;font-weight:700;color:#222;text-decoration:underline;text-decoration-color:var(--sky);text-decoration-thickness:2px}

  .about-title{left:495px;top:567px}
  .about-lead{left:495px;top:636px;width:430px}
  .about-body{left:495px;top:704px;width:430px}
  .about-more{left:495px;top:792px}

  .services-bg{left:0;top:857px;width:1080px;height:613px;background:linear-gradient(90deg,#fff 0 35%,rgba(230,234,236,.8) 60%,#dcdfe0),linear-gradient(#fff,#eef0f1)}
  .services-title{left:143px;top:955px}
  .services-lead{left:143px;top:1026px;width:360px}
  .service-box{top:1095px;width:170px;height:87px;border:2px solid var(--sky);background:rgba(255,255,255,.85);display:flex;flex-direction:column;align-items:center;justify-content:center;gap:8px;font-size:10px;font-weight:700;text-transform:uppercase;color:#222}
  .service-box svg{width:44px;height:34px}
  .bullets{top:1217px;list-style:none;font-size:10.5px;font-weight:600;color:#222;line-height:27px}
  .bullets li::before{content:"";display:inline-block;width:5px;height:5px;border-radius:50%;background:var(--sky);margin-right:9px;vertical-align:middle}
  .call{left:145px;top:1346px;width:332px;height:50px;border:2px solid var(--sky);background:#fff;display:flex;align-items:center;justify-content:center;font-size:28px;color:var(--sky)}
  .call strong{color:#222;font-weight:600;margin-left:10px;font-size:26px}
  .service-photo{left:577px;top:1266px;width:446px;height:284px;background:linear-gradient(150deg,#5b5e63,#9da3a8 45%,#3e4146)}

  .client-photo{left:0;top:1657px;width:341px;height:325px;background:linear-gradient(160deg,#8a7e6c,#c9c3b8 45%,#5b6b4f)}
  .client-title{left:527px;top:1655px}
  .client-lead{left:527px;top:1748px;width:420px}
  .quote{left:527px;top:1798px;font-family:var(--serif);font-size:54px;font-weight:700;color:#222;line-height:1}
  .client-body{left:527px;top:1848px;width:430px}
  .client-more{left:527px;top:1936px}

  .footer-brand{left:145px;top:2082px;font-size:32px}
  .social{left:145px;top:2166px;display:flex;gap:6px}
  .social span{width:27px;height:27px;background:var(--blue)}
  .social span:nth-child(even){background:var(--sky)}
  .links{top:2098px;list-style:none;font-size:10px;color:#444;line-height:20px}
  .contact{left:750px;top:2098px;list-style:none;font-size:10px;color:#555;line-height:15px;width:200px}
  .contact li{display:flex;gap:8px;margin-bottom:8px}
  .contact svg{flex:none;width:11px;height:11px;fill:#555;margin-top:2px}
  .copyright{left:145px;top:2226px;font-size:9.5px;color:#777}
</style>
</head>
<body>
  <div class="board-title responsive">100% RESPONSIVE</div>

  <div class="guide-label font">FONT</div>
  <ul class="font-list">
    <li class="georgia">Georgia - Regular</li>
    <li class="heavy">Futura Hv BT</li>
    <li class="book">Futura Bk BT</li>
  </ul>
  <div class="guide-label color">COLOR</div>
  <div class="swatch" style="top:732px;background:var(--blue)">#0f75bd</div>
  <div class="swatch" style="top:786px;background:var(--sky)">#21abe1</div>
  <div class="swatch" style="top:843px;background:var(--ink)">#363636</div>

  <div class="board-title home">HOME PAGE</div>

  <main class="page">
    <div class="hero" role="img" aria-label="Top-down view of white plumbing pipes, valves and fittings"></div>
    <nav class="nav">
      <a class="active" style="left:0">Home</a>
      <a style="left:66px">About us</a>
      <a style="left:150px">Services</a>
      <a style="left:232px">Testimonials</a>
      <a style="left:337px">Contact us</a>
    </nav>
    <div class="brand hero-brand"><span class="dot"></span>Harbor Pipe</div>

    <div class="photo van" role="img" aria-label="White plumbing service van parked in a driveway"></div>
    <h2 class="about-title">About Harbor Pipe</h2>
    <p class="lead about-lead">Ut enim ad minim veniam, quis nostrud exercitation ullamco laboris nisi ut aliquip ex</p>
    <p class="body about-body">Our licensed crew handles every plumbing job, from a dripping tap to full new construction. We find hidden leaks under slabs and underground, then repair or reroute the line with care. Honest quotes, clean work and fast service.</p>
    <a class="more about-more">Learn More</a>

    <div class="services-bg" role="img" aria-label="Faded photo of a plumber working under a sink"></div>
    <h2 class="services-title">Harbor Pipe Services</h2>
    <p class="lead services-lead">Lorem ipsum dolor sit amet, consectetur adipiscing elit, sed do eiusmod tempor incididunt.</p>

    <div class="service-box" style="left:145px">
      <svg viewBox="0 0 44 34" fill="none" stroke="#0f75bd" stroke-width="2"><rect x="4" y="13" width="22" height="8"/><path d="M26 15h8l6-4M26 19h8l6 4M34 17h8"/></svg>Hydro Jetting</div>
    <div class="service-box" style="left:330px">
      <svg viewBox="0 0 44 34" fill="none" stroke="#0f75bd" stroke-width="2"><path d="M8 6h16v6H14v16H8z"/><path d="M30 18c-3 4-4 6-4 8a4 4 0 0 0 8 0c0-2-1-4-4-8z" fill="#21abe1" stroke="none"/></svg>Leak Detection</div>
    <div class="service-box" style="left:514px">
      <svg viewBox="0 0 44 34" fill="none" stroke="#0f75bd" stroke-width="2"><path d="M12 4v18a6 6 0 0 0 12 0V12h8"/><path d="M28 8v8"/></svg>Drain Cleaning</div>
    <div class="service-box" style="left:696px">
      <svg viewBox="0 0 44 34" fill="none" stroke="#0f75bd" stroke-width="2"><path d="M4 14h36v8H4z"/><path d="M16 14V6h12v8M20 6V2h4v4"/></svg>Mainline Replacement</div>

    <ul class="bullets" style="left:148px">
      <li>Drain Cleaning</li><li>Sewer Line Repairs</li><li>Piping &amp; Repiping</li><li>Leak Detection</li>
    </ul>
    <ul class="bullets" style="left:307px">
      <li>High-Pressure Jetting</li><li>Water Heater Repairs/Installs</li><li>Faucets, sinks &amp; toilet installs/repairs</li><li>Video inspection and sewer repairs</li>
    </ul>
    <div class="call">Call Us : <strong>001-234-5678</strong></div>
    <div class="photo service-photo" role="img" aria-label="Drain cleaning machine on a work site"></div>

    <div class="photo client-photo" role="img" aria-label="Plumber repairing an outdoor water line"></div>
    <h2 class="client-title">What Our Happy<br>Client Says</h2>
    <p class="lead client-lead">Ut enim ad minim veniam, quis nostrud exercitation ullamco laboris nisi ut aliquip ex</p>
    <div class="quote">&ldquo;</div>
    <p class="body client-body">They found the slab leak in under an hour with thermal imaging and fixed it the same day. The crew was polite, tidy and explained every step. Our drains have never run better since the hydro jetting.</p>
    <a class="more client-more">Learn More</a>

    <div class="brand footer-brand"><span class="dot"></span>Harbor Pipe</div>
    <div class="social"><span></span><span></span><span></span><span></span><span></span></div>
    <ul class="links" style="left:432px"><li>Home</li><li>About us</li><li>Services</li><li>Blogs</li></ul>
    <ul class="links" style="left:564px"><li>Testimonials</li><li>Privacy Policy</li><li>Terms &amp; Condition</li><li>Contact Us</li></ul>
    <ul class="contact">
      <li><svg viewBox="0 0 10 10"><path d="M5 0a3.5 3.5 0 0 0-3.5 3.5C1.5 6 5 10 5 10s3.5-4 3.5-6.5A3.5 3.5 0 0 0 5 0zm0 5a1.5 1.5 0 1 1 0-3 1.5 1.5 0 0 1 0 3z"/></svg>214 Harbor Street, Suite 5, Bayview, FL 33101</li>
      <li><svg viewBox="0 0 10 10"><path d="M2 0l2 2.5-1 1.2c.6 1.3 1.6 2.3 2.9 2.9l1.2-1L10 8 8.6 10C4 9.6.4 6 0 1.4z"/></svg>Phone: 001 234 5678</li>
      <li><svg viewBox="0 0 10 10"><path d="M0 2h10v6H0zm1 .6L5 5.4l4-2.8"/></svg>E-mail: info@harborpipe.com</li>
    </ul>
    <p class="copyright">© Copyright 2019 Harbor Pipe. All rights Reserved.</p>
  </main>
</body>
</html>
```